Tobias Webpage Design

I would like to start an business and management consultancy business. I am thinking to called it "Krelto Consultancy". Besides the consultancy services, I would also like to provide training on finance, forensic accounting, fraud prevention and internal control.
Professional management consultants are contracted by organizations to provide advisory services in an objective and independent manner.

Services include, but are not limited to, strategic planning, facilitation, quality assurance, education and training, investment counsel, identification and analysis of management problems, developing solutions, and the implementation of proposed solutions.

Professional management consultants are hired when an organization lacks sufficient resources, requires external objective advice, or because they have expertise not available within the client organization.

I would like to see the webpage design that use colors apple green with some other contrast color. The design have to be professional look but with a new age touch.

Reason: Unable to find a suitable web pages design

Dear all

Since last week I post a request, but till to date, I has yet to received a new sparkling creative and "wow" web page design. Please help me here!

Regards

Reason: Yet to found a suitable web designer for my web design. Help! I just need a fresh and professional look design. You may ignore the color code I prefer. Send me your sparkling creative work. Thank you so much!

Some examples

```html
<!DOCTYPE html>
<html lang="en">
<head>
<meta charset="utf-8">
<title>Krelto Consultancy</title>
<link href="https://fonts.googleapis.com/css2?family=Montserrat:wght@400;500;600;700&family=Roboto+Condensed:wght@700&family=Lora:ital@1&family=Cinzel:wght@400&display=swap" rel="stylesheet">
<style>
:root{
  --green:#7cb518;
  --green-dark:#4f7f0e;
  --red:#e8383d;
  --ink:#1d1d1d;
  --text:#3a3a3a;
  --grey-bg:#eeeeee;
  --panel:#eef3f0;
  --white:#ffffff;
  --sky:#3fa9e0;
}
*{margin:0;padding:0;box-sizing:border-box}
html,body{width:737px;height:1200px;overflow:hidden}
body{position:relative;background:var(--white);font-family:"Montserrat",sans-serif;color:var(--text)}
.abs{position:absolute}

/* hero */
.hero{left:0;top:0;width:737px;height:405px;background:radial-gradient(ellipse at 60% 35%,#b6dd4c 0%,#8dc225 45%,#6ea417 100%);border-top:2px solid var(--red);overflow:hidden}
.nav-home{left:86px;top:2px;width:55px;height:44px;background:rgba(255,255,255,.18)}
.nav a{position:absolute;top:28px;color:var(--white);font-size:11px;font-weight:500;text-decoration:none;letter-spacing:.3px}
.nav-rule{left:86px;top:60px;width:564px;height:1px;background:rgba(255,255,255,.35)}
.brand-mark{left:353px;top:17px;width:30px;height:30px;border-radius:50%;background:var(--white)}
.brand-name{left:300px;top:52px;width:136px;text-align:center;color:var(--white);font-size:11px;font-weight:600}
.hero-title{left:86px;top:106px;font-family:"Roboto Condensed",sans-serif;font-weight:700;line-height:1}
.hero-title .l1{display:block;color:var(--white);font-size:37px;letter-spacing:.5px}
.hero-title .l2{display:block;color:var(--ink);font-size:27px;margin-top:6px;line-height:1.08}
.slogan-art{left:105px;top:216px;width:185px;height:162px;border-radius:8px;background:linear-gradient(135deg,rgba(70,150,215,.55),rgba(220,70,60,.45))}
.portrait{left:430px;top:82px;width:205px;height:323px;background:linear-gradient(180deg,rgba(60,55,55,.35) 0%,rgba(30,30,34,.75) 40%,rgba(25,25,28,.85) 100%)}
.subjects-btn{left:297px;top:240px;z-index:2}
.subjects-btn span{position:absolute;left:18px;top:8px;font-family:"Cinzel",serif;font-size:9.5px;color:var(--white);letter-spacing:.8px;white-space:nowrap}

/* welcome */
.welcome{left:0;top:405px;width:737px;height:317px;background:var(--grey-bg)}
.welcome h1{position:absolute;left:0;top:18px;width:737px;text-align:center;font-size:22px;font-weight:500;color:var(--ink);letter-spacing:.5px}
.welcome .brand-red{font-style:normal;color:var(--red)}
.welcome .intro{position:absolute;left:80px;top:53px;width:577px;text-align:center;font-size:9.6px;line-height:15px}
.service{position:absolute;top:126px;width:181px}
.service .photo{height:86px;border:3px solid var(--white);box-shadow:0 1px 3px rgba(0,0,0,.2)}
.service h2{font-size:12.5px;font-weight:500;color:var(--ink);margin-top:12px}
.service p{font-size:8.2px;line-height:13.5px;margin-top:5px}
.service .more{position:relative;margin-top:10px;height:14px}
.service .more::before{content:"";position:absolute;left:0;right:0;top:7px;height:1px;background:var(--green)}
.service .more span{position:absolute;left:50%;transform:translateX(-50%);width:68px;height:14px;border-radius:7px;background:var(--green);color:var(--white);font-size:7px;text-align:center;line-height:14px}

/* media */
.video-box{left:86px;top:740px;width:405px;height:216px;background:var(--panel)}
.video{left:92px;top:745px;width:277px;height:206px;background:#000}
.video-bar{left:92px;top:929px;width:277px;height:22px;background:#111}
.video-text{left:379px;top:748px;width:108px}
.video-text h3{font-size:13.5px;font-weight:500;color:var(--ink)}
.video-text h3 em{font-style:normal;color:var(--green)}
.video-text p{font-size:8.2px;line-height:13.8px;margin-top:6px}
.feed{left:508px;top:740px;width:142px}
.feed h3{font-size:13.5px;font-weight:500;color:var(--ink);padding-left:30px;line-height:30px;position:relative}
.feed h3::before{content:"";position:absolute;left:2px;top:4px;width:22px;height:22px;border-radius:50%;background:var(--sky)}
.feed h3 em{font-style:normal;color:var(--sky)}
.feed .item{padding:8px 0 9px;border-bottom:1px solid #e2e2e2}
.feed .item strong{display:block;font-size:8.6px;font-weight:600;color:var(--ink);white-space:nowrap}
.feed .item p{font-size:8.2px;line-height:13px;margin-top:3px}

/* testimonials */
.band{left:0;top:972px;width:737px;height:155px;background:var(--grey-bg)}
.block-title{font-size:12.5px;font-weight:500;color:var(--ink);padding-bottom:7px;border-bottom:2px solid var(--green)}
.testi{left:86px;top:993px;width:351px}
.testi-photo{left:88px;top:1028px;width:80px;height:80px;border-radius:50%;border:4px solid #d8e6c5;background:linear-gradient(160deg,#c8cdd2,#4a5560)}
.quote{left:191px;top:1034px;width:248px;font-family:"Lora",serif;font-style:italic;font-size:9px;line-height:14px;color:#444}
.quote cite{display:block;margin-top:5px;color:var(--green);font-size:8.8px}
.quote-mark{left:170px;top:1028px;font-family:"Lora",serif;font-size:30px;color:#c5c5c5;line-height:1}
.message{left:483px;top:993px;width:167px}
.message-banner{left:484px;top:1031px;width:166px;height:65px;border:3px solid var(--white);background:linear-gradient(180deg,#3aa8e4,#1672c2)}

/* footer */
.footer-links{left:86px;top:1146px;font-size:8.5px;color:var(--text)}
.footer-links span{color:#aaa;margin:0 3px}
.social{top:1141px;width:22px;height:22px;border-radius:50%}
.bottom-bar{left:0;top:1175px;width:737px;height:25px;background:var(--green);color:var(--white);font-size:8.5px}
.bottom-bar .copy{position:absolute;left:86px;top:7px}
.bottom-bar .legal{position:absolute;right:87px;top:7px}
</style>
</head>
<body>

<header class="abs hero">
  <div class="abs nav-home"></div>
  <nav class="nav">
    <a style="left:96px">HOME</a>
    <a style="left:156px">ABOUT</a>
    <a style="left:222px">SERVICES</a>
    <a style="left:444px">SUBJECTS</a>
    <a style="left:530px">BLOG</a>
    <a style="left:587px">CONTACT</a>
  </nav>
  <div class="abs brand-mark"></div>
  <div class="abs brand-name">Krelto Consultancy</div>
  <div class="abs nav-rule"></div>

  <h2 class="abs hero-title"><span class="l1">OUR MANAGEMENT,</span><span class="l2">IT and Technology experts are<br>committed to helping you</span></h2>

  <div class="abs slogan-art" role="img" aria-label="Illustration of speech bubbles with short service slogans"></div>
  <div class="abs portrait" role="img" aria-label="Photo of a businesswoman in a dark suit holding a tablet"></div>

  <div class="abs subjects-btn">
    <svg width="150" height="28" viewBox="0 0 150 28"><polygon points="0,14 12,0 150,0 150,28 12,28" fill="#3f6e0c" opacity=".9"/></svg>
    <span>VIEW FOR SUBJECTS</span>
  </div>
</header>

<section class="abs welcome">
  <h1>WELCOME TO <span class="brand-red">KRELTO CONSULTANCY</span></h1>
  <p class="intro">Lorem Ipsum is simply dummy text of the printing and typesetting industry. Lorem Ipsum has been the industry's standard dummy text ever since the 1500s, when an unknown printer took a galley of type and scrambled it to make a type specimen book. It has survived not only five centuries.</p>

  <article class="service" style="left:86px">
    <div class="photo" role="img" aria-label="Photo of a businessman holding a laptop in an office" style="background:linear-gradient(120deg,#d5dde2,#7d8a94)"></div>
    <h2>Financial Training</h2>
    <p>Lorem Ipsum is a simply dummy text of the printing and typesetting industry.</p>
    <div class="more"><span>VIEW MORE</span></div>
  </article>
  <article class="service" style="left:278px">
    <div class="photo" role="img" aria-label="Photo of colleagues in a meeting" style="background:linear-gradient(120deg,#e6e2dc,#8f8a86)"></div>
    <h2>Forensic Accounting</h2>
    <p>Lorem Ipsum is a simply dummy text of the printing and typesetting industry.</p>
    <div class="more"><span>VIEW MORE</span></div>
  </article>
  <article class="service" style="left:470px">
    <div class="photo" role="img" aria-label="Photo of a professional management team" style="background:linear-gradient(120deg,#d9d6d2,#55565a)"></div>
    <h2>Professional Management</h2>
    <p>Lorem Ipsum is a simply dummy text of the printing and typesetting industry.</p>
    <div class="more"><span>VIEW MORE</span></div>
  </article>
</section>

<div class="abs video-box"></div>
<div class="abs video"></div>
<svg class="abs" style="left:207px;top:826px" width="46" height="46" viewBox="0 0 46 46"><circle cx="23" cy="23" r="21" fill="none" stroke="#8a8a8a" stroke-width="2.5"/><polygon points="17,13 33,23 17,33" fill="#8a8a8a"/></svg>
<div class="abs video-bar"></div>
<svg class="abs" style="left:92px;top:922px" width="277" height="29" viewBox="0 0 277 29">
  <rect x="8" y="13" width="3" height="9" fill="#fff"/><rect x="14" y="13" width="3" height="9" fill="#fff"/>
  <rect x="25" y="1" width="24" height="10" fill="#fff"/><text x="37" y="9" font-size="6" text-anchor="middle" fill="#000" font-family="Montserrat,sans-serif">00:00</text>
  <rect x="32" y="14" width="226" height="6" fill="#333" stroke="#555"/>
  <path d="M262 13h3M262 13v3M272 13h-3M272 13v3M262 22h3M262 22v-3M272 22h-3M272 22v-3" stroke="#fff" stroke-width="1.2"/>
</svg>
<div class="abs video-text">
  <h3>View for <em>Krelto</em></h3>
  <p>Lorem Ipsum is simply dummy text of printing and typesetting industry. Lorem Ipsum has been industry's standard the dummy text ever since 1500s, when unknown to printer took galley of type scrambled to make a type specimen book it has survived not only five centuries.</p>
</div>

<aside class="abs feed">
  <h3>Latest <em>Update</em></h3>
  <div class="item"><strong>Lorem Ipsum is simply dummy...</strong><p>Lorem Ipsum is simply dummy the text of typesetting industry.</p></div>
  <div class="item"><strong>Lorem Ipsum is simply dummy...</strong><p>Lorem Ipsum is simply dummy the text of typesetting industry.</p></div>
  <div class="item" style="border:0"><strong>Lorem Ipsum is simply dummy...</strong><p>Lorem Ipsum is simply dummy the text of typesetting industry.</p></div>
</aside>

<section class="abs band"></section>
<div class="abs testi"><div class="block-title">Testimonials</div></div>
<div class="abs testi-photo" role="img" aria-label="Portrait photo of a client"></div>
<div class="abs quote-mark">&ldquo;</div>
<blockquote class="abs quote">Lorem Ipsum has been the industry's standard dummy text ever since the 1500s, when an unknown the printer took a galley of type and scrambled it to make a type specimen book. It has survived not only five centuries.<cite>Arlen Voss</cite></blockquote>
<div class="abs message"><div class="block-title">Send a Message</div></div>
<div class="abs message-banner" role="img" aria-label="Illustrated banner inviting visitors to send a message, with a mailbox"></div>

<nav class="abs footer-links">Home<span>|</span>About<span>|</span>Services<span>|</span>Subjects<span>|</span>Blog<span>|</span>Sitemap<span>|</span>Terms of Use<span>|</span>Connect with us</nav>
<div class="abs social" style="left:570px;background:#2a5a9a"></div>
<div class="abs social" style="left:598px;background:#6c6c6c"></div>
<div class="abs social" style="left:626px;background:#6c6c6c"></div>

<footer class="abs bottom-bar">
  <span class="copy">Copyright © 2013 Marlow Dennet.&nbsp; All Rights Reserved.</span>
  <span class="legal">History | Contact | Privacy</span>
</footer>

</body>
</html>
```